Tolvik cards

I want a simple business card that pops.
Logo on one side.
On side two i want.
"Are you thinking about a new building on your property, or renovating an existing structure? Contact".....
Owners Name: Gary Pellman
Owners Phone number: 555-209-4176
Address:4716 Copper Fern RD, Ashcombe, NV 55018
Committed to Quality, Service, and Integrity

```html
<!DOCTYPE html>
<html lang="en">
<head>
<meta charset="UTF-8">
<title>Tolvik Builders LLC – Business Cards</title>
<link rel="stylesheet" href="https://fonts.googleapis.com/css2?family=Montserrat:wght@400;500;700;800&display=swap">
<style>
  :root {
    --backdrop: #4a4a4c;
    --card-white: #ffffff;
    --brown-dark: #432f1e;
    --brown-text: #4f3a28;
    --brown-accent: #6e4d33;
    --grey-text: #5a514a;
  }
  * { box-sizing: border-box; margin: 0; padding: 0; }
  html, body {
    width: 1200px;
    height: 1200px;
    overflow: hidden;
    background: var(--backdrop);
    font-family: "Montserrat", sans-serif;
  }
  .sheet {
    width: 1200px;
    height: 1200px;
    display: flex;
    flex-direction: column;
    align-items: center;
    justify-content: center;
    gap: 60px;
  }
  .card {
    position: relative;
    width: 900px;
    height: 514px;
    border-radius: 34px;
    overflow: hidden;
  }
  .card--front {
    background: var(--card-white);
    color: var(--brown-text);
  }
  .card--back {
    background: var(--brown-dark);
    display: flex;
    align-items: center;
    justify-content: center;
  }

  /* Front: contact block */
  .contact {
    position: absolute;
    left: 60px;
    top: 72px;
  }
  .contact__name {
    font-size: 38px;
    font-weight: 500;
    letter-spacing: 2px;
    color: var(--grey-text);
    text-transform: uppercase;
  }
  .contact__role {
    font-size: 22px;
    font-weight: 500;
    letter-spacing: 1px;
    color: var(--grey-text);
    margin-bottom: 18px;
  }
  .contact__row {
    display: flex;
    align-items: flex-start;
    gap: 14px;
    font-size: 27px;
    line-height: 1.2;
    color: var(--brown-text);
    margin-bottom: 8px;
  }
  .contact__row svg { flex: 0 0 auto; margin-top: 4px; }
  .contact__tagline {
    margin-top: 20px;
    font-size: 21px;
    font-weight: 700;
    line-height: 1.3;
    color: var(--brown-accent);
  }

  /* Brand name */
  .brand {
    display: flex;
    align-items: center;
    gap: 16px;
  }
  .brand__mark {
    width: 46px;
    height: 46px;
    background: currentColor;
  }
  .brand__text {
    font-weight: 800;
    line-height: 0.95;
  }
  .brand__name { font-size: 70px; letter-spacing: 1px; }
  .brand__sub { font-size: 26px; letter-spacing: 3px; }

  .card--front .brand {
    position: absolute;
    right: 70px;
    top: 72px;
    color: var(--brown-text);
  }
  .card--back .brand {
    color: var(--card-white);
  }
  .card--back .brand__name { font-size: 104px; }
  .card--back .brand__sub { font-size: 36px; letter-spacing: 5px; }
  .card--back .brand__mark { width: 66px; height: 66px; }

  /* Front: call to action */
  .pitch {
    position: absolute;
    left: 0;
    right: 0;
    bottom: 40px;
    text-align: center;
    font-size: 25px;
    font-weight: 700;
    line-height: 1.3;
    color: var(--brown-text);
    padding: 0 60px;
  }
</style>
</head>
<body>
  <main class="sheet">
    <section class="card card--front" aria-label="Business card front">
      <div class="contact">
        <p class="contact__name">Gary Pellman</p>
        <p class="contact__role">OWNER</p>
        <p class="contact__row">
          <svg width="26" height="26" viewBox="0 0 24 24" aria-hidden="true">
            <path fill="#4f3a28" d="M6.6 10.8a15.1 15.1 0 0 0 6.6 6.6l2.2-2.2c.3-.3.7-.4 1-.2 1.1.4 2.3.6 3.6.6.6 0 1 .4 1 1V20c0 .6-.4 1-1 1A17 17 0 0 1 3 4c0-.6.4-1 1-1h3.5c.6 0 1 .4 1 1 0 1.3.2 2.5.6 3.6.1.3 0 .7-.2 1z"/>
          </svg>
          <span>555-209-4176</span>
        </p>
        <p class="contact__row">
          <svg width="26" height="30" viewBox="0 0 24 28" aria-hidden="true">
            <path fill="none" stroke="#4f3a28" stroke-width="2.6" d="M12 26s-8-8.4-8-14a8 8 0 0 1 16 0c0 5.6-8 14-8 14z"/>
            <circle cx="12" cy="12" r="3" fill="#4f3a28"/>
          </svg>
          <span>4716 Copper Fern RD,<br>Ashcombe, NV 55018</span>
        </p>
        <p class="contact__tagline">Committed to Quality,<br>Service, and Integrity</p>
      </div>

      <div class="brand">
        <span class="brand__mark" aria-hidden="true"></span>
        <div class="brand__text">
          <div class="brand__name">TOLVIK</div>
          <div class="brand__sub">BUILDERS LLC</div>
        </div>
      </div>

      <p class="pitch">Are you thinking about a new building on your property,<br>or renovating an existing structure? Contact</p>
    </section>

    <section class="card card--back" aria-label="Business card back">
      <div class="brand">
        <span class="brand__mark" aria-hidden="true"></span>
        <div class="brand__text">
          <div class="brand__name">TOLVIK</div>
          <div class="brand__sub">BUILDERS LLC</div>
        </div>
      </div>
    </section>
  </main>
</body>
</html>
```